Looking for highly visual rework of current Maple Hollow Lodges Wordpress site

Visually Appealing, high tech rework of an existing wordpress site - I want an exquisite sales tool for these gorgeous tiny houses.

Must have the ability to apply various colors and styles to model homes during the sales process. We need to easily create, view, change and save home and color configurations for customers. [Roof Color, Siding, Trim, etc]

Target Market(s)

women, 50 and up

Coding

Coded - Design and coding required

Number of Pages Required

1 page

Font styles to use
Serif

Requirements
Must have
• wordpress compatability
• video of Maple Hollow intro

```html
<!DOCTYPE html>
<html lang="en">
<head>
<meta charset="utf-8">
<title>Maple Hollow Lodges</title>
<link href="https://fonts.googleapis.com/css2?family=Tinos:wght@400;700&display=swap" rel="stylesheet">
<style>
:root{
  --bark:#2f1a0e;
  --wood-dark:#4a2a16;
  --wood:#6b3d20;
  --wood-light:#7f4a28;
  --rust:#b0521c;
  --rust-dark:#8f3f12;
  --olive:#6e7048;
  --gold:#e2b21f;
  --ink:#1f1a17;
  --muted:#6b6460;
  --paper:#ffffff;
  --line:#dcd7d3;
  --soft:#f4f2f0;
}
*{box-sizing:border-box;margin:0;padding:0}
html,body{width:1200px;height:4054px;overflow:hidden}
body{position:relative;background:var(--paper);font-family:"Tinos",serif;color:var(--ink)}
.abs{position:absolute}
.wood{background:linear-gradient(90deg,var(--wood-dark),var(--wood) 30%,var(--wood-light) 55%,var(--wood) 80%,var(--wood-dark))}
.center{text-align:center;left:0;width:1200px}
.btn{position:absolute;display:flex;align-items:center;justify-content:center;color:#fff;border-radius:40px;font-size:15px}
.btn-rust{background:var(--rust)}
.ph{position:absolute}
/* top bar */
.topbar{top:0;left:0;width:1200px;height:32px;background:var(--bark);color:#fff;font-size:12px}
.topbar .phone{left:118px;top:9px}
.topbar .mail{left:536px;top:9px}
.social{position:absolute;display:flex;gap:10px}
.social span{width:14px;height:14px;border-radius:50%;background:#fff;opacity:.85}
/* header */
.header{top:32px;left:0;width:1200px;height:125px}
.order-btn{left:115px;top:40px;width:107px;height:20px;background:#d9b977;color:var(--bark);font-size:11px;border-radius:3px;display:flex;align-items:center;justify-content:center}
.brand{left:470px;top:46px;width:260px;display:flex;align-items:center;justify-content:center;gap:10px;color:#fff;font-size:22px;font-weight:700}
.brand i{width:22px;height:22px;border-radius:50%;background:var(--rust);display:block}
.header-icons{right:118px;top:45px;display:flex;gap:16px}
/* hero */
.hero{top:157px;left:0;width:1200px;height:578px;background:linear-gradient(180deg,#c9d2da 0%,#aeb7bd 40%,#8c5a34 55%,#a45f2c 75%,#8d8a83 100%);border-bottom:5px solid var(--gold)}
.hero-title{top:440px;font-size:31px;color:#fff;line-height:38px}
.play{left:582px;top:395px}
/* headings */
.h2{font-size:30px;color:var(--ink)}
.divider{position:absolute;left:540px;width:120px;height:2px;background:var(--ink)}
.divider::after{content:"";position:absolute;left:54px;top:-5px;width:12px;height:12px;border-radius:50%;background:var(--rust)}
.swatch{top:878px;width:297px;height:233px}
.swatch-label{top:1138px;width:297px;text-align:center;font-size:14px;letter-spacing:.5px}
/* products */
.products{top:1311px;left:0;width:1200px;height:573px}
.product-img{top:1468px;width:211px;height:227px}
.product-name{top:1706px;width:211px;text-align:center;color:#fff;font-size:13px;font-weight:700}
.product-price{top:1728px;width:211px;text-align:center;color:#fff;font-size:12px}
/* gallery */
.tile{width:229px;height:189px}
/* blogs */
.blogs{top:2533px;left:0;width:1200px;height:581px}
.card{top:2649px;width:307px;height:335px;background:#fff}
.card .img{position:absolute;left:14px;top:16px;width:279px;height:179px}
.card .badge{position:absolute;left:22px;top:24px;width:28px;height:34px;background:var(--bark);color:#fff;font-size:9px;text-align:center;line-height:14px;padding-top:3px}
.card h3{position:absolute;left:14px;top:207px;font-size:14px}
.card .meta{position:absolute;left:14px;top:229px;width:279px;font-size:10px;color:var(--muted);display:flex;justify-content:space-between}
.card p{position:absolute;left:14px;top:249px;width:279px;font-size:10.5px;line-height:15px;color:var(--muted)}
.card .more{position:absolute;left:14px;top:291px;font-size:10.5px;color:var(--muted)}
/* newsletter */
.news-input{left:305px;top:3281px;width:587px;height:38px;border:1px solid #bdb6b0;border-radius:20px;font-size:11px;color:#8a837e;padding:12px 20px}
.news-btn{left:765px;top:3281px;width:127px;height:38px;background:var(--bark);border-radius:0 20px 20px 0;color:#fff;font-size:11px;display:flex;align-items:center;justify-content:center}
.perk{top:3395px;width:297px;height:230px;background:var(--soft);text-align:center}
.perk .ic{margin:76px auto 14px;width:40px;height:40px}
.perk h4{font-size:16px;font-weight:700}
.perk small{display:block;font-size:12px;margin-top:4px;color:var(--muted)}
.perk.hot{background:var(--rust);color:#fff}
.perk.hot small{color:#fff}
/* footer */
.footer{top:3663px;left:0;width:1200px;height:391px;color:#fff}
.foot-brand{left:122px;top:3740px;display:flex;align-items:center;gap:8px;font-size:19px;font-weight:700;color:#fff}
.foot-brand i{width:18px;height:18px;border-radius:50%;background:var(--rust);display:block}
.foot-text{left:122px;top:3822px;width:250px;font-size:13px;line-height:16px;color:#fff}
.cards{left:122px;top:3882px;display:flex;gap:6px}
.cards span{width:36px;height:22px;background:#fff;border-radius:2px}
.foot-h{top:3750px;font-size:13px;font-weight:700;color:#fff}
.foot-h::after{content:"";display:block;width:28px;height:1px;background:var(--rust);margin-top:5px}
.links{left:420px;top:3794px;font-size:11.5px;line-height:17px;list-style:none}
.links li::before{content:"› ";color:#fff}
.office{left:598px;top:3794px;font-size:11.5px;line-height:16px;list-style:none}
.office li{display:flex;gap:12px;margin-bottom:6px}
.office svg{flex:none;margin-top:2px}
.field{position:absolute;height:24px;border:1px solid rgba(255,255,255,.25);background:rgba(0,0,0,.15);font-size:10px;padding:5px 8px;color:#e8dccf}
.copyright{top:4014px;left:0;width:1200px;height:40px;background:var(--bark);color:#fff;font-size:12px}
</style>
</head>
<body>

<!-- top bar -->
<div class="abs topbar">
  <span class="abs phone">+01 555-014-229</span>
  <span class="abs mail">info@maplehollowlodges.com</span>
  <div class="social" style="left:940px;top:9px"><span></span><span></span><span></span><span></span><span style="background:var(--gold)"></span></div>
</div>

<!-- header -->
<header class="abs header wood">
  <div class="abs order-btn">Order Form</div>
  <div class="abs brand"><i></i>Maple Hollow Lodges</div>
  <div class="abs header-icons">
    <svg width="14" height="14" viewBox="0 0 14 14" fill="none" stroke="#fff" stroke-width="1.6"><circle cx="6" cy="6" r="4.5"/><path d="M9.5 9.5 13 13"/></svg>
    <svg width="14" height="14" viewBox="0 0 14 14" fill="none" stroke="#fff" stroke-width="1.6"><circle cx="7" cy="4.5" r="3"/><path d="M1.5 13.5c0-3 2.5-5 5.5-5s5.5 2 5.5 5"/></svg>
    <svg width="16" height="14" viewBox="0 0 16 14" fill="none" stroke="#fff" stroke-width="1.6"><path d="M1 1h2.5l2 8h8l1.5-6H4.5"/><circle cx="6.5" cy="12" r="1.2"/><circle cx="12.5" cy="12" r="1.2"/></svg>
    <svg width="14" height="14" viewBox="0 0 14 14" fill="#fff"><rect y="2" width="14" height="2"/><rect y="6" width="14" height="2"/><rect y="10" width="14" height="2"/></svg>
  </div>
</header>

<!-- hero -->
<section class="abs hero" role="img" aria-label="Intro video still of a cedar-sided tiny house with red metal roof on a trailer"></section>
<svg class="abs play" width="36" height="36" viewBox="0 0 36 36"><circle cx="18" cy="18" r="17" fill="none" stroke="#fff" stroke-width="2"/><path d="M14 11l11 7-11 7z" fill="#fff"/></svg>
<h1 class="abs center hero-title" style="font-weight:400">Your Satisfactions is Our<br>Customization</h1>

<!-- colors -->
<h2 class="abs center h2" style="top:800px;font-weight:400">Check Out Some of Our New Colors</h2>
<div class="divider" style="top:846px"></div>
<div class="abs swatch" style="left:122px;background:linear-gradient(160deg,#8a6a4c,#c9a27a 60%,#6d5038)" role="img" aria-label="Cabin interior in Wheat finish"></div>
<div class="abs swatch" style="left:454px;background:linear-gradient(180deg,#c7d0cf,#8f7a58 45%,#6b5a3e 80%,#9aa08a)" role="img" aria-label="Cabin in Alder siding with copper penny roof"></div>
<div class="abs swatch" style="left:784px;background:linear-gradient(180deg,#d6dde3,#a49e97 40%,#7c7670 85%)" role="img" aria-label="Cabin in Silver Ash siding"></div>
<div class="abs swatch-label" style="left:122px">WHEAT</div>
<div class="abs swatch-label" style="left:454px">ALDER &amp; COPPER PENNY ROOF</div>
<div class="abs swatch-label" style="left:784px">SILVER ASH</div>
<div class="btn btn-rust" style="left:262px;top:1211px;width:327px;height:46px;font-size:17px;border:2px solid #7a3510">Standard Features</div>
<div class="btn" style="left:614px;top:1211px;width:327px;height:46px;font-size:17px;background:var(--olive);border:2px solid #52543a">Upgrade Options</div>

<!-- feature products -->
<section class="abs products wood"></section>
<div class="abs center" style="top:1356px;color:#fff;font-size:13px">Maple Hollow</div>
<div class="abs" style="top:1378px;left:560px;width:80px;height:2px;background:#fff"></div>
<div class="abs" style="top:1374px;left:595px;width:10px;height:10px;border-radius:50%;background:var(--rust)"></div>
<h2 class="abs center" style="top:1390px;color:#fff;font-size:30px;font-weight:700">Feature Product</h2>
<svg class="abs" style="left:1026px;top:1400px" width="46" height="22" viewBox="0 0 46 22"><circle cx="11" cy="11" r="10" fill="var(--rust)"/><path d="M13 6l-5 5 5 5" stroke="#fff" stroke-width="2" fill="none"/><circle cx="35" cy="11" r="10" fill="none" stroke="var(--rust)" stroke-width="1.5"/><path d="M33 6l5 5-5 5" stroke="var(--rust)" stroke-width="2" fill="none"/></svg>

<div class="abs product-img" style="left:122px;background:linear-gradient(180deg,#b9bfc4,#6f675f 55%,#8a8478)" role="img" aria-label="Grey cabin model on a lot"></div>
<div class="btn btn-rust" style="left:157px;top:1568px;width:140px;height:34px;font-size:13px">Shop Now</div>
<svg class="abs" style="left:192px;top:1610px" width="72" height="14" viewBox="0 0 72 14" fill="none" stroke="#fff" stroke-width="1.4"><path d="M7 12C2 8 1 6 1 4.5 1 2.5 2.5 1 4.2 1 5.5 1 6.5 2 7 3c.5-1 1.5-2 2.8-2C11.5 1 13 2.5 13 4.5 13 6 12 8 7 12z"/><circle cx="36" cy="6" r="4.5"/><path d="M39.5 9.5 42 12"/><circle cx="61" cy="7" r="1.6"/><circle cx="69" cy="2.5" r="1.6"/><circle cx="69" cy="11.5" r="1.6"/><path d="M62.5 6.2 67.5 3.3M62.5 7.8l5 2.9"/></svg>
<div class="abs product-img" style="left:368px;background:linear-gradient(180deg,#cfd6dc,#a53a2a 45%,#8d3326 75%,#9b9486)" role="img" aria-label="Red cabin model with white trim"></div>
<div class="abs product-img" style="left:616px;background:linear-gradient(180deg,#b8c9d6,#b84a2a 35%,#9c5a2c 70%,#7a6a4c)" role="img" aria-label="Cedar cabin with red roof and porch lattice"></div>
<div class="abs product-img" style="left:865px;background:linear-gradient(180deg,#c4ccd2,#b4522a 40%,#a35a2c 75%,#8f8a80)" role="img" aria-label="Tiny house on wheels with cedar siding"></div>
<div class="abs product-name" style="left:122px">Product Name 01</div><div class="abs product-price" style="left:122px">$00.00</div>
<div class="abs product-name" style="left:368px">Product Name 02</div><div class="abs product-price" style="left:368px">$00.00</div>
<div class="abs product-name" style="left:616px">Product Name 03</div><div class="abs product-price" style="left:616px">$00.00</div>
<div class="abs product-name" style="left:865px">Product Name 04</div><div class="abs product-price" style="left:865px">$00.00</div>
<div class="btn btn-rust" style="left:522px;top:1797px;width:156px;height:36px;font-size:12px">View All</div>

<!-- gallery -->
<h2 class="abs center h2" style="top:1930px;font-weight:400">Gallery</h2>
<div class="abs tile" style="left:122px;top:2000px;background:linear-gradient(135deg,#5a3a24,#a07a55 55%,#3a2a20)" role="img" aria-label="Living room with stone fireplace"></div>
<div class="abs tile" style="left:365px;top:2000px;background:linear-gradient(135deg,#c49a62,#a8773f 60%,#3f5a9a)" role="img" aria-label="Pine-paneled room with blue sofa"></div>
<div class="abs tile" style="left:608px;top:2000px;background:linear-gradient(180deg,#d8d4c6,#c8b48c 60%,#8e8a70)" role="img" aria-label="Screened porch with white railings"></div>
<div class="abs tile" style="left:851px;top:2000px;background:linear-gradient(135deg,#c88a4c,#9a5e2c 60%,#5c3a22)" role="img" aria-label="Kitchen with wood cabinets"></div>
<div class="abs tile" style="left:122px;top:2203px;background:linear-gradient(135deg,#e0c08a,#c49a5e 60%,#6a4a2a)" role="img" aria-label="Pine kitchen with black stove"></div>
<div class="abs tile" style="left:365px;top:2203px;background:linear-gradient(135deg,#a8743e,#c9955a 55%,#e9e4dc)" role="img" aria-label="Bedroom with wood walls"></div>
<div class="abs tile" style="left:608px;top:2203px;background:linear-gradient(135deg,#d7c0a0,#b99468 50%,#3e5a96)" role="img" aria-label="Sitting area with recliners"></div>
<div class="abs tile" style="left:851px;top:2203px;background:linear-gradient(135deg,#d4b486,#a8844e 55%,#7b7268)" role="img" aria-label="Kitchen with stainless range"></div>
<div class="btn btn-rust" style="left:522px;top:2444px;width:156px;height:36px;font-size:12px">View All</div>

<!-- blogs -->
<section class="abs blogs wood"></section>
<h2 class="abs center" style="top:2578px;color:#fff;font-size:30px;font-weight:400">Our Blogs</h2>
<div class="abs center" style="top:2616px;color:#fff;font-size:12px">Lorem Ipsum is simply dummy text the Printing.</div>

<article class="abs card" style="left:111px">
  <div class="img" style="background:linear-gradient(180deg,#c9d2d8,#a9652c 40%,#7e6a4c 85%)" role="img" aria-label="Cabin with cedar siding and porch"></div>
  <div class="badge">01<br>Oct</div>
  <h3>Blog Post Heading</h3>
  <div class="meta"><span>▢ October 05, 2018</span><span>◯ 20 &nbsp; ♡ 12</span></div>
  <p>Lorem Ipsum is simply dummy text of the And printing and typesetting industry.</p>
  <div class="more">Read More.. ›</div>
</article>
<article class="abs card" style="left:446px">
  <div class="img" style="background:linear-gradient(180deg,#d4c39c,#9a6a3c 40%,#5a4430 85%)" role="img" aria-label="Covered cabin porch with wood posts"></div>
  <div class="badge">01<br>Oct</div>
  <h3>Blog Post Heading</h3>
  <div class="meta"><span>▢ October 06, 2018</span><span>◯ 20 &nbsp; ♡ 12</span></div>
  <p>Lorem Ipsum is simply dummy text of the printing and typesetting industry.</p>
  <div class="more">Read More.. ›</div>
</article>
<article class="abs card" style="left:781px">
  <div class="img" style="background:linear-gradient(180deg,#cfd5da,#8c8579 45%,#6e675c 85%)" role="img" aria-label="Grey cabin exterior"></div>
  <div class="badge">01<br>Oct</div>
  <h3>Blog Post Heading</h3>
  <div class="meta"><span>▢ October 07, 2018</span><span>◯ 20 &nbsp; ♡ 12</span></div>
  <p>Lorem Ipsum is simply dummy text of the printing and typesetting industry.</p>
  <div class="more">Read More.. ›</div>
</article>
<div class="btn btn-rust" style="left:522px;top:3034px;width:156px;height:34px;font-size:12px">View All</div>

<!-- newsletter -->
<h2 class="abs center h2" style="top:3196px;font-weight:400">Join Our Newsletter</h2>
<div class="abs center" style="top:3240px;font-size:11px;color:var(--muted)">Sign up for Our Newsletter</div>
<div class="abs news-input">Email Here</div>
<div class="abs news-btn">Subscribe</div>

<div class="abs perk" style="left:119px">
  <svg class="ic" viewBox="0 0 40 40"><rect x="6" y="10" width="28" height="22" rx="3" fill="var(--rust)"/><path d="M13 21l5 5 9-10" stroke="#fff" stroke-width="3" fill="none"/></svg>
  <h4>100 Satisfaction</h4><small>Satisfaction Guarantee</small>
</div>
<div class="abs perk hot" style="left:449px">
  <svg class="ic" viewBox="0 0 40 40"><circle cx="20" cy="14" r="7" fill="#fff"/><path d="M7 36c0-8 6-13 13-13s13 5 13 13z" fill="#fff"/><path d="M11 14a9 9 0 0 1 18 0" stroke="#fff" stroke-width="2" fill="none"/></svg>
  <h4>24/7 Customer Services</h4><small>Call us 24/7 at 000 555 0142</small>
</div>
<div class="abs perk" style="left:778px">
  <svg class="ic" viewBox="0 0 40 40"><path d="M20 5c9 0 15 6 15 13s-6 13-15 13c-2 0-4 0-6-1l-7 4 2-7c-3-2-4-5-4-9 0-7 6-13 15-13z" fill="var(--rust-dark)"/><text x="20" y="24" font-family="Tinos,serif" font-size="14" font-weight="700" fill="#fff" text-anchor="middle">?</text></svg>
  <h4>Product Guide</h4><small>How to Shop</small>
</div>

<!-- footer -->
<footer class="abs footer wood"></footer>
<div class="abs foot-brand"><i></i>Maple Hollow</div>
<p class="abs foot-text">Lorem Ipsum is simply dummy text of the printing and typesetting industry. Lorem Ipsum has been the industry's</p>
<div class="abs cards"><span></span><span></span><span></span><span></span><span></span></div>

<div class="abs foot-h" style="left:414px">Quick Links</div>
<ul class="abs links"><li>Home</li><li>Cabins</li><li>Gallery</li><li>Construction</li><li>Options</li><li>DEALER</li><li>Contact us</li></ul>

<div class="abs foot-h" style="left:624px">Office</div>
<ul class="abs office">
  <li><svg width="10" height="13" viewBox="0 0 10 13"><path d="M5 0a5 5 0 0 1 5 5c0 4-5 8-5 8S0 9 0 5a5 5 0 0 1 5-5z" fill="#fff"/><circle cx="5" cy="5" r="1.8" fill="var(--wood)"/></svg><span>48 Birch Lane,<br>Fernvale, USA<br>TX 00000</span></li>
  <li><svg width="11" height="11" viewBox="0 0 11 11"><path d="M2 0l2 3-1 1.5c1 1.5 2 2.5 3.5 3.5L8 7l3 2-1 2C5 11 0 6 0 1z" fill="#fff"/></svg><span>000 555 014 2290</span></li>
  <li><svg width="12" height="9" viewBox="0 0 12 9"><rect width="12" height="9" fill="#fff"/><path d="M0 0l6 5 6-5" stroke="var(--wood)" fill="none"/></svg><span>Sales@maplehollowlodges.com</span></li>
  <li><svg width="11" height="11" viewBox="0 0 11 11"><circle cx="5.5" cy="5.5" r="5.5" fill="#fff"/><path d="M5.5 2.5v3h2.5" stroke="var(--wood)" fill="none"/></svg><span>Mon-Sat 9:00am-6 :00pm</span></li>
</ul>

<div class="abs foot-h" style="left:816px">Quick Contact</div>
<div class="field" style="left:816px;top:3790px;width:130px">Name</div>
<div class="field" style="left:956px;top:3790px;width:130px">Phone</div>
<div class="field" style="left:816px;top:3822px;width:270px;height:62px">Message</div>
<div class="btn btn-rust" style="left:956px;top:3896px;width:130px;height:22px;font-size:11px">Send</div>

<div class="abs copyright">
  <span class="abs" style="left:118px;top:13px">© Copyright 2018 Maple Hollow. All Rights Reserved</span>
  <div class="social" style="left:900px;top:10px;gap:12px"><span style="width:20px;height:20px;background:var(--rust);opacity:1"></span><span style="width:20px;height:20px;background:var(--rust);opacity:1"></span><span style="width:20px;height:20px;background:var(--rust);opacity:1"></span><span style="width:20px;height:20px;background:var(--rust);opacity:1"></span><span style="width:20px;height:20px;background:var(--rust);opacity:1"></span></div>
</div>

</body>
</html>
```